Flyer : Wolkenbank - Emphatisches Zuhören
Zielgruppe
Hallo und vielen Dank für dein Interesse an diesem Projekt.
Nachstehend ein paar Gedanken, die ein Gefühl für das Ziel des zu entwickelnden Flyers hervorrufen soll.
1. Warum gibt es Wolkenbank? (Das Fundament)
Das Problem:
In einer zunehmend beschleunigten und digitalen Welt vereinsamen Menschen – oft auch inmitten eines vollen Alltags. Freunde und Familie sind häufig überfordert, voreingenommen oder neigen dazu, sofort ungefragte Ratschläge zu verteilen, statt einfach nur zuzuhören.
Die Mission:
Wolkenbank.de bietet einen geschützten, wertfreien Raum, in dem Menschen einfach sein und reden dürfen. Es geht nicht um Therapie, sondern um das befreiende Gefühl, auf Augenhöhe gehört und verstanden zu werden. Der Name impliziert bereits die Gemütlichkeit und Sicherheit eines Sessels gepaart mit offenen Ohren.
2. Was leistet Wolkenbank?
Das Angebot:
- Professionelle Präsenz: Echtes, aktives und empathisches Zuhören ohne Bewertung.
- Entlastung: Raum für Gedanken und Gefühle, die man sonst nirgends aussprechen mag (Mental Load abbauen).
- Flexibilität: Niedrigschwelliger Zugang ohne monatelange Wartezeiten.
3. Zielgruppen-Matrix
Erwartung vs. Nutzen:
Für den Flyer ist es genial, die Zielgruppen direkt in ihren jeweiligen Bedürfnissen abzuholen. Hier ist eine Übersicht, die visuell übersetzt werden sollte.
Zielgruppe 1:
- Überlastete Berufstätige, Führungskräfte und Care-Arbeiter
Erwartung/Schmerzpunkt:
- „Ich funktioniere nur noch. Niemand hört mir zu, ohne dass es gleich um Lösungen geht.“
Der Wolkenbank-Nutzen:
- Ventil & Me-Time: Ein Raum, um den Ballast des Tages abzuwerfen, ganz ohne Erwartungsdruck.
Zielgruppe 2:
- Einsame oder ältere Menschen
- „Ich möchte einfach mal wieder ein echtes, tiefes Gespräch führen, das über das Wetter hinausgeht.“
Aufgabenstellung
Tonalität & Visuelle Identität (Look & Feel)
Empathisch, warm und einladend, aber hochgradig professionell. Der Flyer darf weder klinisch-kalt (wie eine Arztpraxis) noch esoterisch-verspielt wirken.
Farbpsychologie: Setzt auf beruhigende, vertrauenserweckende Töne (gern Orientierung an die Website), warme Erdtöne, sanftes Lila. Keine aggressiven Primärfarben (wie Knallrot oder Signalgelb).
Bildsprache: Vermeidet sterile Stockfotos von Menschen mit „Fake-Lächeln“. Besser sind authentische, ruhige Motive: Fokussierte Details (z. B. eine dampfende Tasse Kaffee, ein gemütlicher Sessel im Anschnitt) oder abstrakte Formen, die das Thema „Resonanz“ und „Zuhören“ symbolisieren (z. B. Wellenlinien, die sanft ineinandergreifen).
Format & Struktur des Flyers
Format: Eure Empfehlung, vielleicht ein 6-seitiger Wickelfalz-Flyer (DIN lang). Das könnte folgende Struktur ergeben:
Titelseite: Das Kernversprechen („Emphatisches Zuhören - Zeit und Raum für unvoreingenommenes Zuhören und Mitteilen) + Logo.
Innenseiten (3 Spalten): Perfekt, um die 3 oben genannten Zielgruppen getrennt voneinander mit ihren spezifischen Erwartungen und dem Wolkenbank-Nutzen anzusprechen.
Rückseite / Innere Klappe: Der Ablauf (Wie buche ich ein Gespräch?) und der klare Call to Action (CTA) inklusive Website-Adresse sowie Kontaktdaten.
Technische & Textliche Vorgaben
Barrierefreiheit & Lesbarkeit:
Da auch ältere Menschen zur Zielgruppe gehören, muss die Typografie klar, kontrastreich und ausreichend groß sein (keine filigranen Light-Schriften auf hellem Grund).
Auf dem Flyer kann ein prominenter Hinweis platziert werden, der Zugang zur Website (oder auch Infos eines Blogbeitrags mit weiteren Erklärungen zum Angebot) beinhaltet, z. B. via eines QR-Code, der die entsprechende URL enthält. Etwas, das man mitnehmen kann, wenn man den Flyer nicht einstecken möchte...

```html
<!DOCTYPE html>
<html lang="de">
<head>
<meta charset="utf-8">
<title>Wolkenbank – Empathisches Zuhören</title>
<link href="https://fonts.googleapis.com/css2?family=Barlow:ital,wght@0,400;0,500;0,600;0,700;0,800;1,600;1,700&display=swap" rel="stylesheet">
<style>
  :root{
    --stage:#9d9d9d;
    --paper:#f6f4f0;
    --purple:#8e3797;
    --mauve:#935a72;
    --pink:#d4357b;
    --ink:#3a3a3a;
    --white:#ffffff;
  }
  *{box-sizing:border-box;margin:0;padding:0}
  html,body{width:852px;height:1200px;overflow:hidden}
  body{background:var(--stage);font-family:'Barlow',sans-serif;color:var(--ink);position:relative}
  .sheet{position:absolute;left:67px;width:718px;height:508px;display:flex;background:var(--paper);box-shadow:4px 6px 10px rgba(0,0,0,.35)}
  .sheet--outside{top:67px}
  .sheet--inside{top:624px}
  .panel{position:relative;width:239.33px;height:100%;overflow:hidden}
  .panel + .panel{border-left:1px solid #e6e2dd}
  .center{text-align:center}
  .abs{position:absolute;left:0;right:0}
  .heading{font-weight:700;color:var(--purple);font-size:19px;line-height:1.45}
  .rule{position:absolute;left:50%;width:52px;margin-left:-26px;height:1px;background:var(--pink)}
  .body-text{font-size:8.6px;line-height:1.55}
  .photo{position:absolute}

  /* Formats panel */
  .format-card{position:absolute;left:18px;width:202px;height:70px;border:1px solid var(--pink);border-radius:8px;display:flex;align-items:center;padding-left:10px}
  .heart-dot{flex:none;border-radius:50%;background:var(--mauve);display:flex;align-items:center;justify-content:center}
  .format-card .heart-dot{width:42px;height:42px}
  .format-card .info{margin-left:11px}
  .format-card h3{font-size:8.6px;font-weight:600;line-height:1.5;color:#222}
  .format-card p{font-size:6.6px;line-height:1.55;margin-top:3px;color:#444}

  /* Contact panel */
  .panel--contact{background:var(--mauve);color:var(--white)}
  .contact-title{font-size:19px;font-weight:600;line-height:1.3}
  .contact-rule{background:var(--white)}
  .contact-intro{font-size:7px;font-weight:600;line-height:1.6}
  .contact-row{position:absolute;left:52px;right:20px;display:flex;gap:8px;font-size:8.8px;line-height:1.5}
  .contact-row svg{flex:none;margin-top:2px}
  .contact-divider{position:absolute;left:52px;width:126px;height:1px;background:rgba(255,255,255,.45)}

  /* Cover panel */
  .brand{font-weight:500;color:var(--purple);letter-spacing:.5px;display:flex;align-items:center;justify-content:center;gap:6px}
  .brand .dot{width:9px;height:9px;border-radius:50%;background:var(--pink)}
  .cover-kicker{left:20px;font-size:7.4px;letter-spacing:2px;color:#444}
  .cover-title{left:20px;font-size:27px;font-weight:800;color:var(--purple);line-height:1.1}
  .cover-sub{left:20px;right:20px;font-size:7px;font-weight:600;color:var(--pink);line-height:1.55}
  .cover-note{left:20px;right:18px;font-size:4.8px;line-height:1.6;color:#444}
  .cover-cta{left:20px;font-size:11px;font-weight:600;text-decoration:underline;color:#333}

  /* Values list */
  .value-list{list-style:none;position:absolute;left:24px;top:269px}
  .value-list li{display:flex;align-items:center;height:35px;font-size:8.8px;line-height:1.5}
  .value-list .heart-dot{width:25px;height:25px;margin-right:6px}
  .accent{font-size:8.8px;font-weight:600;color:var(--pink)}
  .quote{font-style:italic;font-weight:700;color:var(--purple);font-size:8.6px;line-height:1.55}

  /* Check lists */
  .check-list{list-style:none;position:absolute}
  .check-list li{display:flex;align-items:flex-start;font-size:8.8px;line-height:1.5;margin-bottom:9px}
  .check{flex:none;width:13px;height:13px;border-radius:2px;background:var(--mauve);display:flex;align-items:center;justify-content:center;margin-right:10px;margin-top:0}
</style>
</head>
<body>

<section class="sheet sheet--outside">

  <div class="panel panel--formats">
    <h2 class="abs center heading" style="top:53px">Wir nehmen<br>uns Zeit für Sie</h2>
    <div class="rule" style="top:124px"></div>
    <p class="abs center body-text" style="top:141px;padding:0 30px">Wählen Sie das Gesprächsformat, das am besten zu Ihnen passt.</p>

    <div class="format-card" style="top:193px">
      <span class="heart-dot"><svg width="20" height="18" viewBox="0 0 24 22"><path d="M12 21s-9-6-9-12a5 5 0 0 1 9-3 5 5 0 0 1 9 3c0 6-9 12-9 12z" fill="#fff"/></svg></span>
      <div class="info"><h3>Einzelgespräch<br>vor Ort</h3><p>Persönliches Gespräch in angenehmer Atmosphäre.</p></div>
    </div>
    <div class="format-card" style="top:273px">
      <span class="heart-dot"><svg width="20" height="18" viewBox="0 0 24 22"><path d="M12 21s-9-6-9-12a5 5 0 0 1 9-3 5 5 0 0 1 9 3c0 6-9 12-9 12z" fill="#fff"/></svg></span>
      <div class="info"><h3>Einzelgespräch per<br>Video</h3><p>Flexibel. Bequem. Von überall<br>erreichbar.</p></div>
    </div>
    <div class="format-card" style="top:353px">
      <span class="heart-dot"><svg width="20" height="18" viewBox="0 0 24 22"><path d="M12 21s-9-6-9-12a5 5 0 0 1 9-3 5 5 0 0 1 9 3c0 6-9 12-9 12z" fill="#fff"/></svg></span>
      <div class="info"><h3>Einzelgespräch<br>telefonisch</h3><p>Diskret. Einfach. Ganz ohne<br>Anfahrt.</p></div>
    </div>
  </div>

  <div class="panel panel--contact">
    <h2 class="abs center contact-title" style="top:165px">Lassen Sie<br>uns zuhören.</h2>
    <div class="rule contact-rule" style="top:224px"></div>
    <p class="abs center contact-intro" style="top:237px;padding:0 18px">Sie haben Fragen?<br>Wir begleiten Sie mit Offenheit, Wertschätzung und echtem Interesse.</p>

    <div class="contact-row" style="top:334px">
      <svg width="10" height="11" viewBox="0 0 24 24"><path d="M6 2l4 5-2 3c1 3 3 5 6 6l3-2 5 4-3 4C10 22 2 14 2 5z" fill="none" stroke="#fff" stroke-width="2"/></svg>
      <span>01234 555 01 23</span>
    </div>
    <div class="contact-divider" style="top:364px"></div>
    <div class="contact-row" style="top:379px">
      <svg width="10" height="12" viewBox="0 0 24 28"><path d="M12 26s-9-9-9-15a9 9 0 0 1 18 0c0 6-9 15-9 15z" fill="none" stroke="#fff" stroke-width="2"/><circle cx="12" cy="11" r="3" fill="none" stroke="#fff" stroke-width="2"/></svg>
      <span>Lindenweg 7, 12345<br>Musterdorf (Nahe Musterstadt)</span>
    </div>
    <div class="contact-divider" style="top:422px"></div>
    <div class="contact-row" style="top:439px">
      <svg width="11" height="9" viewBox="0 0 24 18"><rect x="1" y="1" width="22" height="16" fill="none" stroke="#fff" stroke-width="2"/><path d="M1 1l11 9 11-9" fill="none" stroke="#fff" stroke-width="2"/></svg>
      <span>info@wolkenbank.de</span>
    </div>
  </div>

  <div class="panel panel--cover">
    <div class="photo" role="img" aria-label="Foto: rosa Sessel mit kleinem Beistelltisch und Laptop vor hellen Vorhängen" style="left:0;right:0;top:240px;bottom:0;background:linear-gradient(180deg,#f6f4f0 0%,#efe3e0 25%,#e7c3c1 55%,#dcc4bd 80%,#d9d2cb 100%)"></div>
    <div class="abs brand" style="top:28px;font-size:17px"><span class="dot"></span>Wolkenbank</div>
    <p class="abs cover-kicker" style="top:80px">WILLKOMMEN BEI WOLKENBANK</p>
    <h1 class="abs cover-title" style="top:95px">EMPATHISCHES<br>ZUHÖREN</h1>
    <p class="abs cover-sub" style="top:158px">Hier finden Sie Zeit und Raum für unvoreingenommenes Zuhören und Mitteilen.</p>
    <p class="abs cover-note" style="top:198px">Manchmal braucht es keinen Rat. Manchmal genügt ein Mensch, der einfach zuhört.<br>Bei Wolkenbank stehen Sie mit Ihren Gedanken und Gefühlen im Mittelpunkt.</p>
    <p class="abs cover-cta" style="top:222px">Einfach reden. Einfach gehört werden.</p>
  </div>
</section>

<section class="sheet sheet--inside">

  <div class="panel panel--values">
    <div class="photo" role="img" aria-label="Foto: weiße Vase mit Eukalyptuszweig" style="left:90px;right:0;top:260px;bottom:0;background:radial-gradient(ellipse at 65% 70%,#e4e6df 0%,#eceae5 45%,rgba(246,244,240,0) 75%)"></div>
    <h2 class="abs center heading" style="top:27px">Wo das Zuhören im<br>Mittelpunkt steht</h2>
    <div class="rule" style="top:97px"></div>
    <p class="abs center body-text" style="top:111px;padding:0 22px">Wir bieten einen geschützten Raum für Ihre Gedanken und Gefühle.</p>
    <p class="abs center quote" style="top:155px">Ohne Urteil<br>Ohne Bewertung.<br>Ohne ungefragte Empfehlungen.</p>
    <p class="abs center body-text" style="top:203px;padding:0 12px">Bei uns finden Sie ein offenes Ohr, das aufmerksam zuhört und Ihnen auf Augenhöhe begegnet.</p>
    <p class="abs center accent" style="top:249px">Dafür stehen wir</p>
    <ul class="value-list">
      <li><span class="heart-dot"><svg width="12" height="11" viewBox="0 0 24 22"><path d="M12 21s-9-6-9-12a5 5 0 0 1 9-3 5 5 0 0 1 9 3c0 6-9 12-9 12z" fill="#fff"/></svg></span>Empathisches<br>Zuhören</li>
      <li><span class="heart-dot"><svg width="12" height="11" viewBox="0 0 24 22"><path d="M12 21s-9-6-9-12a5 5 0 0 1 9-3 5 5 0 0 1 9 3c0 6-9 12-9 12z" fill="#fff"/></svg></span>Menschlichkeit</li>
      <li><span class="heart-dot"><svg width="12" height="11" viewBox="0 0 24 22"><path d="M12 21s-9-6-9-12a5 5 0 0 1 9-3 5 5 0 0 1 9 3c0 6-9 12-9 12z" fill="#fff"/></svg></span>Vertrauen</li>
      <li><span class="heart-dot"><svg width="12" height="11" viewBox="0 0 24 22"><path d="M12 21s-9-6-9-12a5 5 0 0 1 9-3 5 5 0 0 1 9 3c0 6-9 12-9 12z" fill="#fff"/></svg></span>Respekt</li>
      <li><span class="heart-dot"><svg width="12" height="11" viewBox="0 0 24 22"><path d="M12 21s-9-6-9-12a5 5 0 0 1 9-3 5 5 0 0 1 9 3c0 6-9 12-9 12z" fill="#fff"/></svg></span>Diskretion</li>
      <li><span class="heart-dot"><svg width="12" height="11" viewBox="0 0 24 22"><path d="M12 21s-9-6-9-12a5 5 0 0 1 9-3 5 5 0 0 1 9 3c0 6-9 12-9 12z" fill="#fff"/></svg></span>Zeit für Sie</li>
    </ul>
  </div>

  <div class="panel panel--why">
    <h2 class="abs center heading" style="top:44px">Warum</h2>
    <div class="abs brand" style="top:94px;font-size:28px"><span class="dot" style="width:14px;height:14px"></span>Wolkenbank</div>
    <div class="rule" style="top:173px"></div>
    <p class="abs center body-text" style="top:190px;padding:0 18px">Jeder Mensch erlebt Zeiten, in denen Gedanken und Gefühle schwer werden.</p>
    <p class="abs center body-text" style="top:229px">Nicht immer braucht es eine Therapie.</p>
    <p class="abs center body-text" style="top:255px">Nicht immer möchte man Lösungen hören.</p>
    <p class="abs center body-text" style="top:281px;padding:0 40px">Oft hilft es bereits, alles aussprechen zu dürfen.</p>
    <p class="abs center accent" style="top:325px">Wir bieten Ihnen</p>
    <ul class="check-list" style="left:44px;top:350px">
      <li style="margin-bottom:12px"><span class="check"><svg width="8" height="7" viewBox="0 0 12 10"><path d="M1 5l3.5 3.5L11 1" fill="none" stroke="#fff" stroke-width="2"/></svg></span>Raum zum Reden</li>
      <li style="margin-bottom:12px"><span class="check"><svg width="8" height="7" viewBox="0 0 12 10"><path d="M1 5l3.5 3.5L11 1" fill="none" stroke="#fff" stroke-width="2"/></svg></span>Aufmerksamkeit ohne Bewertung</li>
      <li style="margin-bottom:12px"><span class="check"><svg width="8" height="7" viewBox="0 0 12 10"><path d="M1 5l3.5 3.5L11 1" fill="none" stroke="#fff" stroke-width="2"/></svg></span>Entlastung durch Zuhören</li>
      <li style="margin-bottom:12px"><span class="check"><svg width="8" height="7" viewBox="0 0 12 10"><path d="M1 5l3.5 3.5L11 1" fill="none" stroke="#fff" stroke-width="2"/></svg></span>Neue Klarheit für eigene<br>Entscheidungen</li>
      <li><span class="check"><svg width="8" height="7" viewBox="0 0 12 10"><path d="M1 5l3.5 3.5L11 1" fill="none" stroke="#fff" stroke-width="2"/></svg></span>Gespräche auf Augenhöhe</li>
    </ul>
  </div>

  <div class="panel panel--offer">
    <div class="photo" role="img" aria-label="Foto: Tasse Tee auf Korkuntersetzer neben Strickdecke auf Holztisch" style="left:0;right:0;top:300px;bottom:0;background:linear-gradient(180deg,rgba(246,244,240,0) 0%,#e4ddd3 25%,#c9b39a 60%,#a7784b 100%)"></div>
    <h2 class="abs center heading" style="top:27px">Unser Angebot<br>für Sie</h2>
    <div class="rule" style="top:97px"></div>
    <p class="abs center" style="top:111px;font-size:12px;font-weight:600;color:var(--pink)">Einfach da sein dürfen</p>
    <p class="abs body-text" style="top:146px;left:23px">Unser Angebot richtet sich an Menschen,</p>
    <ul class="check-list" style="left:23px;top:169px;right:14px">
      <li style="margin-bottom:12px"><span class="check"><svg width="8" height="7" viewBox="0 0 12 10"><path d="M1 5l3.5 3.5L11 1" fill="none" stroke="#fff" stroke-width="2"/></svg></span>die sich überlastet fühlen</li>
      <li style="margin-bottom:12px"><span class="check"><svg width="8" height="7" viewBox="0 0 12 10"><path d="M1 5l3.5 3.5L11 1" fill="none" stroke="#fff" stroke-width="2"/></svg></span>die sich einsam fühlen</li>
      <li style="margin-bottom:12px"><span class="check"><svg width="8" height="7" viewBox="0 0 12 10"><path d="M1 5l3.5 3.5L11 1" fill="none" stroke="#fff" stroke-width="2"/></svg></span>die einen geschützten Gesprächspartner suchen</li>
      <li style="margin-bottom:12px"><span class="check"><svg width="8" height="7" viewBox="0 0 12 10"><path d="M1 5l3.5 3.5L11 1" fill="none" stroke="#fff" stroke-width="2"/></svg></span>die ihre Gedanken ordnen möchten</li>
      <li><span class="check"><svg width="8" height="7" viewBox="0 0 12 10"><path d="M1 5l3.5 3.5L11 1" fill="none" stroke="#fff" stroke-width="2"/></svg></span>die einfach einmal erzählen möchten.</li>
    </ul>
  </div>
</section>

</body>
</html>
```